Packaging Design Project - new spa massage oils brand

We need a packaging design for the products of a new line of oil for massage to be used at spas or by independent professionals. The brand name is "lumina", it's reminiscent of that ethereal moment where you lose track of the day-to-day and focus on yourself while being taken care off with aromatherapy, relaxing music and massage.
The packaging is a 250 ml transparent plastic bottle, the design will be in two labels, a front label with the brand and main design elements (product, net content, brand name) and a back label with more generic info. Both labels are of the same size 4.5 x 9 cm. A picture of the bottle will be provided in a separate file along with some ideas.
We are a start-up company in latin america, therefore the texts should be in spanish. There will be initially four SKU's, however, since we don't have a budget for all, we'll use the winning design and I'll use that as a base to create the other labels.
the four initial SKUs are:
-Rosemary (green pallet of colors)
-Lavender (purple pallet)
-Citrus (orange, yellow)
-Baby (pastels, predominantly blue)
We would expect you to focus on either the rosemary or lavender SKU's since those are our most important ones.
We don't have a logo yet for two reasons 1) budget constraints, 2) less restrictions for you to create the packaging artwork. If it's possible to add a mock-up of a logo it would be great.

the text for the back label (spanish) is:
Una combinación natural de aceites de semillas, flores y plantas para un masaje corporal relajante.
PRECAUCIONES: Mantener fuera del alcance de los niños. Evite el contacto con los ojos.
Este producto es biodegradable. No daña la capa de ozono.

translation (not to be on the lable, only for reference).
a combination of natural oils of seeds, flowers and plants for a relaxing body massage.
WARNING: keep out of reach of children, avoid eye contact.
this product is biodegradable. it doesn't damage the ozone layer.

Front label (spanish):
- lumina (this is the brand name)
- Aceite para masaje corporal con extracto de romero (this is the product description oil for body massage with rosemary extract)
- Frescura y vitalidad (this means freshness and vitality which are the characteristics of the rosemary oil)
- 250 ml (this is the net content)

Target Market(s)

consider that this product is used by professionals, however, the end consumers are mostly women (but not exclusive) of 30-45 years old.

Industry/Entity Type

Baby

Requirements
Nice to have
• -If the proposal could have a logo (even a simple one) it would be very much appreciated.
-Might want to try getting inspiration from other "ethereal" things such as smoke, watter ripples, air, fire, etc.
-A distinctive element of what the product has (for instance a picture or a sketch of a rosemary twig or a lavender flower).
-Colors are very important for these type of products, the whole pallet should be consistent. Consider that the rosemary oil is dark green, lavender is clear.
Should not have
• -Aggressive or excessively bright colors (this is a relaxation product).
-If you consider using a smoke texture, it should avoid dark, black shades that smoke usually evanesces into.
-Too polluted labels.

```html
<!DOCTYPE html>
<html lang="es">
<head>
<meta charset="utf-8">
<title>lumina – etiquetas aceite para masaje</title>
<link rel="stylesheet" href="https://fonts.googleapis.com/css2?family=Marcellus&family=Josefin+Sans:wght@400&family=Crimson+Text:ital@0;1&display=swap">
<style>
  :root{
    --bg:#ffffff;
    --label:#ffffff;
    --ink:#5b5b5b;
    --soft:#8a8a8a;
    --rule:#c9c9c9;
    --green:#8cb92d;
    --green-dark:#5f8f1c;
    --green-light:#c9df97;
    --purple:#9a2d7c;
    --purple-dark:#7e2466;
    --purple-light:#dcc0d6;
  }
  *{margin:0;padding:0;box-sizing:border-box}
  html,body{width:1200px;height:1083px;overflow:hidden;background:var(--bg)}
  .sheet{position:relative;width:1200px;height:1083px}
  .label{position:absolute;top:262px;width:270px;height:560px;background:var(--label);
    box-shadow:0 0 0 1px #e4e4e4;overflow:hidden}
  .label--back{left:112px}
  .label--rosemary{left:465px}
  .label--lavender{left:818px}

  .brand{position:absolute;top:40px;left:0;right:0;display:flex;align-items:center;justify-content:center;gap:8px}
  .brand__dot{width:14px;height:14px;border-radius:50%}
  .brand__name{font-family:"Marcellus",serif;font-size:30px;letter-spacing:1px;color:var(--ink)}
  .label--rosemary .brand__dot{background:var(--green)}
  .label--lavender .brand__dot,.label--back .brand__dot{background:var(--purple)}

  .art{position:absolute;left:60px;right:60px;top:110px;height:110px;border-radius:50% 50% 0 0}
  .label--rosemary .art{background:linear-gradient(180deg,rgba(140,185,45,.05),rgba(140,185,45,.45))}
  .label--lavender .art{background:linear-gradient(180deg,rgba(154,45,124,.05),rgba(154,45,124,.35))}

  .band{position:absolute;left:0;right:0;top:222px;height:130px;color:#fff;text-align:center;
    display:flex;flex-direction:column;justify-content:center;align-items:center}
  .label--rosemary .band{background:var(--green);border-bottom:6px solid var(--green-dark)}
  .label--lavender .band{background:var(--purple);border-bottom:6px solid var(--purple-dark)}
  .band__product{font-family:"Marcellus",serif;font-size:40px;letter-spacing:1px;line-height:1}
  .band__dots{width:200px;border-top:3px dotted rgba(255,255,255,.9);margin:12px 0 8px}
  .band__claim{font-family:"Josefin Sans",sans-serif;font-size:15px;letter-spacing:1.5px}

  .desc{position:absolute;top:380px;left:0;right:0;text-align:center;
    font-family:"Josefin Sans",sans-serif;font-size:21px;line-height:1.2;color:var(--ink)}
  .label--rosemary .accent{color:var(--green-dark)}
  .label--lavender .accent{color:var(--purple)}
  .net{position:absolute;right:22px;bottom:46px;font-family:"Josefin Sans",sans-serif;font-size:14px;color:var(--ink)}

  .back__frame{position:absolute;inset:14px;border:1px dotted var(--rule)}
  .back__art{position:absolute;right:16px;top:150px;width:110px;height:130px;
    background:linear-gradient(200deg,rgba(154,45,124,.18),rgba(154,45,124,0));border-radius:40% 0 0 40%}
  .back__text{position:absolute;left:30px;right:26px;font-family:"Crimson Text",serif;color:var(--ink)}
  .back__intro{top:130px;font-style:italic;font-size:14px;line-height:1.3;text-align:center}
  .back__warning{top:235px;font-size:16px;line-height:1.3;text-align:justify}
  .back__eco{top:330px;font-size:16px;line-height:1.3;text-align:center}
  .back__seal{position:absolute;left:50%;top:440px;width:26px;height:26px;margin-left:-13px;border-radius:50%;background:var(--green)}
</style>
</head>
<body>
<main class="sheet">

  <section class="label label--back" aria-label="Etiqueta posterior">
    <div class="back__frame"></div>
    <div class="brand"><span class="brand__dot"></span><span class="brand__name">lumina</span></div>
    <div class="back__art" role="img" aria-label="Ilustración tenue de ramas florales en lila"></div>
    <p class="back__text back__intro">Una combinación natural de aceites de semillas, flores y plantas para un masaje corporal relajante.</p>
    <p class="back__text back__warning">PRECAUCIONES: Mantener fuera del alcance de los niños. Evite el contacto con los ojos.</p>
    <p class="back__text back__eco">Este producto es biodegradable. No daña la capa de ozono.</p>
    <div class="back__seal" aria-label="Sello de reciclaje"></div>
  </section>

  <section class="label label--rosemary" aria-label="Etiqueta frontal Rosemary">
    <div class="brand"><span class="brand__dot"></span><span class="brand__name">lumina</span></div>
    <div class="art" role="img" aria-label="Ilustración de ramitas de romero en verdes suaves"></div>
    <div class="band">
      <h2 class="band__product">ROSEMARY</h2>
      <div class="band__dots"></div>
      <p class="band__claim">FRESCURA Y VITALIDAD</p>
    </div>
    <p class="desc"><span class="accent">Aceite para</span><br>masaje<br><span class="accent">corporal</span><br>con extracto<br><span class="accent">de romero.</span></p>
    <p class="net">250 ml</p>
  </section>

  <section class="label label--lavender" aria-label="Etiqueta frontal Lavanda">
    <div class="brand"><span class="brand__dot"></span><span class="brand__name">lumina</span></div>
    <div class="art" role="img" aria-label="Ilustración de flores de lavanda en tonos lila"></div>
    <div class="band">
      <h2 class="band__product">LAVANDA</h2>
      <div class="band__dots"></div>
      <p class="band__claim">FRESCURA Y VITALIDAD</p>
    </div>
    <p class="desc"><span class="accent">Aceite para</span><br>masaje<br><span class="accent">corporal</span><br>con extracto<br><span class="accent">de romero.</span></p>
    <p class="net">250 ml</p>
  </section>

</main>
</body>
</html>
```